BrightOak Cards, letterhead, and envelopes
BrightOak Technologies and Rx
BrightOak Cards, letterhead, and envelopes - Information Technology
Creative Brief
Use same font as used in my logo
or as you see fit
Professional
Thomas R. Perlavic
President, CEO
4817 S. Harlan Crest Avenue Suite 300
tperlavic@BrightOakTech.example
www.BrightOakTech.example
On the front of the business card please use the BrightOak Technologies logo, the BrightOakTech.example website, and integrate the i graphic with a shadow effect. On the back of the business card, please use the square logo (i with the Rx), the i graphic with the shadow effect and list the BrightOakRx.example website.

```html
<!DOCTYPE html>
<html lang="en">
<head>
<meta charset="utf-8">
<title>BrightOak Business Cards</title>
<link href="https://fonts.googleapis.com/css2?family=Montserrat:wght@400;600;800&family=Open+Sans:wght@400;600;700&display=swap" rel="stylesheet">
<style>
  :root {
    --bg: #e9e6e1;
    --navy: #1f3a6e;
    --blue: #2f5d9e;
    --sky: #6d9fd6;
    --green: #6e9b2b;
    --lime: #9cc24a;
    --ink: #1d2f52;
    --white: #ffffff;
  }
  * { margin: 0; padding: 0; box-sizing: border-box; }
  html, body { width: 1200px; height: 901px; overflow: hidden; background: var(--bg); }
  .canvas { position: relative; width: 1200px; height: 901px; }
  .card {
    position: absolute; width: 520px; height: 300px; border-radius: 14px; overflow: hidden;
    box-shadow: 0 10px 28px rgba(0,0,0,.18);
  }
  .card svg { position: absolute; inset: 0; }
  .card-back { left: 60px; top: 130px; background: linear-gradient(160deg, var(--blue), var(--navy)); }
  .card-front { left: 620px; top: 470px; background: var(--white); }

  .back-mark { position: absolute; left: 150px; top: 110px; display: flex; align-items: center; gap: 16px; }
  .back-mark .tile { width: 80px; height: 80px; border-radius: 14px; background: var(--white); }
  .back-mark .name { font-family: 'Montserrat', sans-serif; font-weight: 800; font-size: 38px; color: var(--white); }

  .front-logo {
    position: absolute; right: 40px; top: 58px;
    font-family: 'Montserrat', sans-serif; font-weight: 800; font-size: 46px; color: var(--ink); letter-spacing: -0.5px;
  }
  .person { position: absolute; right: 44px; top: 168px; text-align: center; font-family: 'Open Sans', sans-serif; color: var(--ink); }
  .person .name { font-weight: 700; font-size: 14px; }
  .person .title { font-size: 12px; margin-top: 2px; }
  .contact {
    position: absolute; left: 22px; top: 186px;
    font-family: 'Open Sans', sans-serif; font-size: 10.5px; line-height: 1.45; color: var(--white);
  }
</style>
</head>
<body>
<main class="canvas">
  <section class="card card-back" aria-label="Business card back">
    <div class="back-mark">
      <span class="tile"></span>
      <span class="name">BrightOak</span>
    </div>
  </section>

  <section class="card card-front" aria-label="Business card front">
    <svg width="520" height="300" viewBox="0 0 520 300" aria-hidden="true">
      <defs>
        <linearGradient id="blueBand" x1="0" y1="0" x2="1" y2="1">
          <stop offset="0" stop-color="#2f5d9e"/>
          <stop offset="1" stop-color="#1f3a6e"/>
        </linearGradient>
      </defs>
      <path class="band-blue" d="M0,150 C170,150 300,265 520,238 L520,300 L0,300 Z" fill="url(#blueBand)"/>
      <path class="band-sky" d="M200,230 C320,290 430,270 520,252 L520,300 L260,300 Z" fill="#6d9fd6" opacity=".55"/>
      <path class="swoosh-green" d="M0,140 C180,132 310,250 520,222" fill="none" stroke="#6e9b2b" stroke-width="7"/>
      <path class="swoosh-lime" d="M0,128 C190,118 320,236 520,208" fill="none" stroke="#9cc24a" stroke-width="3"/>
    </svg>
    <div class="front-logo">BrightOak</div>
    <div class="person">
      <div class="name">Thomas R. Perlavic</div>
      <div class="title">President, CEO</div>
    </div>
    <div class="contact">
      4817 S. Harlan Crest Avenue<br>
      Suite 300<br>
      P: 555.201.4830 &nbsp;|&nbsp; C: 555.318.2965<br>
      E: tperlavic@BrightOakTech.example<br>
      www.BrightOakTech.example
    </div>
  </section>
</main>
</body>
</html>
```